"Jewelry Line Postcard Design"

Would like to describe what the line is about via a bio include a photo of me and the logo.

Target Market(s)

20-55

Industry/Entity Type

Jewelry

```html
<!DOCTYPE html>
<html lang="en">
<head>
<meta charset="utf-8">
<title>Aria Vela — Jewelry Line Postcard</title>
<link href="https://fonts.googleapis.com/css2?family=Carlito:ital,wght@0,400;0,700;1,400&family=Noto+Serif:ital@1&display=swap" rel="stylesheet">
<style>
  :root {
    --stage: #e9eaec;
    --ink-black: #000000;
    --paper: #ffffff;
    --lilac: #b98cc9;
    --plum: #8b3f8f;
    --accent: #a0265f;
    --photo-light: #cfcfcf;
    --photo-dark: #3a3a3a;
    --photo-frame: #dcdcdc;
  }
  * { box-sizing: border-box; margin: 0; padding: 0; }
  html, body {
    width: 1200px; height: 1000px; overflow: hidden;
    background: var(--stage);
  }
  .postcard {
    position: absolute; left: 50px; top: 74px;
    width: 1100px; height: 852px;
    background: var(--paper);
    font-family: "Carlito", "Calibri", sans-serif;
  }
  .bio-panel {
    position: absolute; left: 0; top: 0;
    width: 1100px; height: 587px;
    background: var(--ink-black);
  }
  .bio-line {
    position: absolute; display: block;
    height: 44px; line-height: 44px;
    font-size: 22px; color: var(--lilac);
    text-align: justify; text-align-last: justify;
    white-space: nowrap;
  }
  .bio-line.end { text-align-last: left; }
  .bio-line b { font-weight: 700; }
  .col-left-wide { left: 57px; width: 475px; }
  .col-left { left: 57px; width: 295px; }
  .col-right-wide { left: 571px; width: 475px; }
  .col-right { left: 746px; width: 300px; }
  .portrait {
    position: absolute; left: 378px; top: 156px;
    width: 344px; height: 431px;
    border: 3px solid var(--photo-frame); border-bottom: none;
    background: linear-gradient(180deg, var(--photo-light) 0%, #9a9a9a 55%, var(--photo-dark) 100%);
  }
  .brand-name {
    position: absolute; left: 63px; top: 720px;
    display: flex; align-items: center; gap: 14px;
    font-size: 52px; font-weight: 400; color: var(--ink-black);
    letter-spacing: 2px;
  }
  .brand-mark { width: 14px; height: 14px; background: var(--accent); }
  .brand-quote {
    position: absolute; right: 53px; top: 668px;
    font-family: "Noto Serif", Georgia, serif; font-style: italic;
    font-size: 20px; line-height: 28px; color: var(--plum);
    text-align: right;
  }
</style>
</head>
<body>
<main class="postcard">
  <section class="bio-panel">
    <span class="bio-line col-left-wide" style="top:46px">• <b>DR. LENA MARLOW</b> has had a love affair</span>
    <span class="bio-line col-left-wide" style="top:90px">with jewelry for as long as she can remember.</span>
    <span class="bio-line col-left" style="top:133px">Perhaps it started way</span>
    <span class="bio-line col-left" style="top:177px">back in the day, when she</span>
    <span class="bio-line col-left" style="top:220px">religiously use to look</span>
    <span class="bio-line col-left" style="top:264px">through her grandmother’s</span>
    <span class="bio-line col-left end" style="top:308px">jewelry box.</span>
    <span class="bio-line col-left" style="top:351px">• Her current collection is</span>
    <span class="bio-line col-left" style="top:395px"><b>ARIA VELA</b> (<i>BIG DREAMS</i></span>
    <span class="bio-line col-left" style="top:438px">in Romanian). These pieces</span>
    <span class="bio-line col-left" style="top:482px">are based on the bold and</span>

    <span class="bio-line col-right-wide" style="top:46px">dramatic costume pieces of the 60’s and 70’s.</span>
    <span class="bio-line col-right-wide" style="top:90px">Everyone deserves to feel Glamorous and</span>
    <span class="bio-line col-right" style="top:133px">beautiful. This collection is</span>
    <span class="bio-line col-right" style="top:177px">a great way to step into your</span>
    <span class="bio-line col-right end" style="top:220px">most stunning self.</span>
    <span class="bio-line col-right" style="top:264px">• Dr. Lena’s jewelry has been</span>
    <span class="bio-line col-right" style="top:308px">worn by stylists, designers,</span>
    <span class="bio-line col-right" style="top:351px">high profile TV personalities</span>
    <span class="bio-line col-right" style="top:395px">and anchors, as well as</span>
    <span class="bio-line col-right" style="top:438px">people who just want to look</span>
    <span class="bio-line col-right end" style="top:482px">good and feel beautiful.</span>

    <div class="portrait" role="img" aria-label="Black and white portrait photo of the jewelry designer"></div>
  </section>

  <div class="brand-name"><span class="brand-mark"></span>ARIA VELA</div>

  <p class="brand-quote">
    “It’s my goal to make every woman feel like<br>
    her very best self, so she can go out into the<br>
    world to sparkle and shine. To create a line of<br>
    jewelry that’s both beautiful and purposeful is<br>
    truly a dream come true.”
  </p>
</main>
</body>
</html>
```